Redesign our website!

Tandlo’ current web (http://tandlo-example.com) site was implemented in 2012 and needs to be brought up to date with look and feel of our new packaging and logo. The layout of Tandlo’ website is fairly consistent from page to page; utilizing only two very similar “templates” or “themes.”

Tandlo is seeking a designer to gain inspiration from our new packaging, design and recent print ad and create a new look for our website (http://tandlo-example.com); focusing on the wallpaper, background, navigation bars/buttons, header and footer. Additionally, Tandlo needs a new “style” for the images used in the slideshow on the homepage as well as the banner images on the product category/subcategory pages.

It is important that element height/width and positioning of elements (such as the "feature" boxes on the homepage, navigation bar, and banner images) within the pages are not changed in the new design. In other words, this project is solely focused on the overall design, not the specific layouts of each page.

Attached are:
* a zip file of JPEG examples of our new packaging;
* a pdf copy of a print ad we recently used for an industry tradeshow;
* a zip file with 2 JPEGS of images used in our booth at the above mentioned tradeshow;
* a JPEG of our new logo;
* a JPEG of the Background used on our new packing.

The model images that can be used in the mock-up of the new homepage slideshow but please do not feel as though you need to use the models in your banner mock-up. If you use your own models (stock images are OK,) please try to incorporate our products on the models.This will help us get a realistic sense of your direction.

I am very encouraged by the examples I am seeing. Thank you to those who have contributed and to those still working on it, please do! This is by no means a done deal with any one design.

One tip to those who have already contributed and those still to do so: we are looking for a new color scheme. Please do not use the brown/green you see on the current site.  Thank you.

• Remove "Vines" from the background"
Change the header to less look "yoga"ish
1 "sample" image for the homepage slideshow
1 "sample image" for a category banner (i.e. the banner on http://tandlo-example.com/quorvets/)

```html
<!DOCTYPE html>
<html lang="en">
<head>
<meta charset="utf-8">
<title>Tandlo — Quorvets Wrist Wallets</title>
<link href="https://fonts.googleapis.com/css2?family=Comfortaa:wght@300;400;700&family=Open+Sans:wght@400;600;700&display=swap" rel="stylesheet">
<style>
:root{
  --blue:#1a7fd3;
  --yellow:#fbe21a;
  --slate:#5b5d62;
  --ink:#111;
  --text:#555;
  --muted:#777;
  --white:#fff;
  --line:#d8d8d8;
  --chalk:#2b2c2f;
}
*{box-sizing:border-box;margin:0;padding:0}
html,body{width:951px;height:1200px;overflow:hidden;background:var(--white)}
body{position:relative;font-family:"Open Sans",Arial,sans-serif;color:var(--text)}
.abs{position:absolute}
.display{font-family:"Comfortaa",sans-serif}

/* header backdrop */
.header-bg{left:0;top:0;width:951px;height:525px}
.brand{left:148px;top:14px;font-family:"Comfortaa",sans-serif;font-weight:700;font-size:36px;color:var(--white);letter-spacing:-1px}
.top-links{right:147px;top:16px;font-size:9.5px;color:var(--ink);word-spacing:2px;white-space:nowrap}
.top-links b{font-weight:700;margin:0 3px}
.phone-row{left:516px;top:37px;display:flex;align-items:center;gap:6px;font-size:12.5px;color:var(--ink)}
.dot{width:18px;height:18px;border-radius:50%;background:var(--ink);display:inline-block}
.dot-phone{display:flex;align-items:center;justify-content:center}
.socials{left:623px;top:37px;display:flex;gap:6px}
.search{left:700px;top:38px;width:102px;height:18px;background:var(--white);font-size:8px;color:#999;padding:4px 8px;border-radius:1px}
.search svg{position:absolute;right:5px;top:4px}

/* navigation */
.nav{left:148px;top:72px;width:654px;height:31px;background:#0b0b0b;font-family:"Comfortaa",sans-serif;font-size:11px;color:var(--white)}
.nav span{position:absolute;top:9px;white-space:nowrap}
.nav .active{color:var(--yellow)}

/* hero */
.hero{left:148px;top:103px;width:654px;height:379px;background:linear-gradient(135deg,#e4e4e4,#f4f4f4 45%,#ffffff);overflow:hidden}
.hero-photo{left:250px;top:0;width:404px;height:379px;background:linear-gradient(90deg,rgba(255,255,255,0) 0,rgba(230,230,232,.6) 22%,#b88d74 42%,#2a3446 55%,#1f2a3c 78%,#3a4456 90%,#c29a80 100%)}
.hero-title{left:44px;top:86px;font-size:27px;font-weight:400;color:var(--ink);letter-spacing:-.3px;white-space:nowrap}
.hero-sub{left:46px;top:126px;width:310px;font-family:Arial,sans-serif;font-size:12px;line-height:14.5px;color:#666}
.hero-list{left:46px;top:169px;width:314px;display:grid;grid-template-columns:158px 156px;font-family:Arial,sans-serif;font-size:10px;color:#222}
.hero-list li{list-style:none;height:24px;display:flex;align-items:center;gap:5px;border-bottom:1px solid #e2e2e2;white-space:nowrap}
.hero-btn{left:44px;top:221px;width:212px;height:35px;background:var(--blue);color:var(--white);font-family:"Comfortaa",sans-serif;font-size:13px;display:flex;align-items:center;justify-content:center;outline:1px dashed rgba(255,255,255,.7);outline-offset:-3px}
.slide-arrow{width:31px;height:31px;border-radius:50%;background:rgba(120,120,120,.55);display:flex;align-items:center;justify-content:center;top:263px}

/* newsletter */
.newsletter{left:148px;top:482px;width:654px;height:43px;background:#0b0b0b}
.newsletter .label{left:20px;top:13px;font-family:"Comfortaa",sans-serif;font-size:13px;color:var(--white);white-space:nowrap}
.field{top:12px;height:20px;background:var(--white);font-family:Arial,sans-serif;font-size:9.5px;color:#999;padding:4px 12px}
.subscribe{left:518px;top:12px;width:124px;height:20px;background:var(--blue);color:var(--white);font-family:"Comfortaa",sans-serif;font-size:9.5px;display:flex;align-items:center;justify-content:center}

/* content */
.section-title{font-family:"Comfortaa",sans-serif;font-size:14.5px;font-weight:400;color:var(--ink);display:flex;align-items:center;gap:5px;white-space:nowrap}
.section-title::after{content:"";flex:1;border-top:1px dashed #555}
.more-btn{left:510px;top:562px;width:88px;height:13px;background:var(--blue);color:var(--white);font-size:7px;display:flex;align-items:center;justify-content:center}
.intro{left:148px;top:590px;width:460px;font-size:8.7px;line-height:13px;color:#555;letter-spacing:-.05px}
.card{width:225px;height:128px;border:1px solid var(--line);background:var(--white);padding:5px;box-shadow:0 1px 2px rgba(0,0,0,.08)}
.card .pic{width:100%;height:100%}
.plus{position:absolute;right:14px;bottom:13px;width:15px;height:15px;border-radius:50%;background:var(--blue);color:var(--white);font-size:13px;line-height:14px;text-align:center;font-weight:700}
.card-title{font-size:10px;font-weight:600;color:var(--ink);white-space:nowrap}
.card-desc{font-size:9px;line-height:10px;color:var(--muted);width:225px}
.promo-box{left:634px;top:583px;width:168px;height:308px;border:1px solid var(--line);background:var(--white)}
.promo-art{left:20px;top:15px;width:130px;height:280px;background:linear-gradient(180deg,#46474a 0,#37383b 30%,#4a7fb8 45%,#3a3b3e 62%,#2e2f32 86%,#f3d21f 90%,#f6d623 100%)}
.mini-arrow{width:14px;height:14px;border-radius:50%;background:#222;display:flex;align-items:center;justify-content:center;top:716px}

/* footer */
.footer{left:0;top:916px;width:951px;height:216px;background:linear-gradient(180deg,#2e2f31,#26272a)}
.footer-band{left:0;top:1132px;width:951px;height:6px;background:var(--yellow)}
.foot-head{top:42px;font-family:"Comfortaa",sans-serif;font-size:13px;font-weight:400;color:var(--yellow);white-space:nowrap}
.foot-links{top:64px;list-style:none;font-size:8.6px;color:#e8e8e8}
.foot-links li{height:21.5px;display:flex;align-items:center;gap:6px;border-bottom:1px solid #4a4b4e;padding-left:4px;white-space:nowrap}
.foot-links li:last-child{border-bottom:none}
.foot-links li::before{content:"›";color:#aaa;font-size:9px}
.news{left:378px;width:230px;display:flex;gap:8px}
.news .date{font-family:"Comfortaa",sans-serif;color:var(--yellow);font-size:10px;line-height:13px;width:38px;white-space:nowrap}
.news .date b{display:block;font-size:12.5px;font-weight:400}
.news .body{font-size:8.6px;line-height:10.3px;color:#ddd;white-space:nowrap}
.news .body strong{color:var(--white);font-weight:700}
.social-ring{width:33px;height:33px;border-radius:50%;background:#f2f2f2;top:71px}
.contact{left:633px;font-size:11.5px;color:var(--white);display:flex;align-items:center;gap:7px;white-space:nowrap}
.contact .f{color:var(--blue)}
.connect{left:633px;top:166px;width:169px;height:27px;background:var(--blue);color:var(--white);font-family:"Comfortaa",sans-serif;font-size:12.5px;display:flex;align-items:center;justify-content:center;outline:1px dashed rgba(255,255,255,.7);outline-offset:-3px}
.legal{left:148px;top:1154px;font-size:7.8px;line-height:10px;color:#777}
.foot-brand{right:149px;top:1150px;font-family:"Comfortaa",sans-serif;font-weight:700;font-size:20px;color:#a6a6a6}
</style>
</head>
<body>

<svg class="abs header-bg" viewBox="0 0 951 525" aria-hidden="true">
  <rect width="951" height="525" fill="#5b5d62"/>
  <rect width="422" height="330" fill="#1a7fd3"/>
  <rect x="422" width="529" height="330" fill="#fbe21a"/>
  <polygon points="0,324 951,184 951,525 0,525" fill="#5b5d62"/>
</svg>

<div class="abs brand">Tandlo</div>
<div class="abs top-links">Home <b>/</b> About <b>/</b> Contact <b>/</b> Signin <b>/</b> Signup <b>/</b> Checkout <b>/</b> Cart : 01</div>
<div class="abs phone-row">
  <span class="dot dot-phone"><svg width="9" height="9" viewBox="0 0 24 24"><path fill="#fff" d="M6.6 10.8a15 15 0 006.6 6.6l2.2-2.2c.3-.3.7-.4 1-.2 1.1.4 2.3.6 3.6.6.6 0 1 .4 1 1V20c0 .6-.4 1-1 1A17 17 0 013 4c0-.6.4-1 1-1h3.5c.6 0 1 .4 1 1 0 1.3.2 2.5.6 3.6.1.3 0 .7-.2 1z"/></svg></span>
  <span>555-318-2740</span>
</div>
<div class="abs socials" role="img" aria-label="Social network links"><span class="dot"></span><span class="dot"></span><span class="dot"></span></div>
<div class="abs search">Search
  <svg width="8" height="8" viewBox="0 0 10 10"><circle cx="4" cy="4" r="3" fill="none" stroke="#888" stroke-width="1.2"/><line x1="6.3" y1="6.3" x2="9.3" y2="9.3" stroke="#888" stroke-width="1.3"/></svg>
</div>

<nav class="abs nav">
  <span style="left:22px">Quorvets Brist Wallets</span>
  <span class="active" style="left:172px">Earvelts Ear Warmers</span>
  <span style="left:319px">Apparel</span>
  <span style="left:391px">Accessories</span>
  <span style="left:486px">Eco Products</span>
  <span style="left:589px">Blog</span>
</nav>

<section class="abs hero">
  <div class="abs hero-photo" role="img" aria-label="Runner in a dark athletic shirt wearing a teal waist wallet, with white earbuds in the foreground"></div>
  <h1 class="abs hero-title display">Quorvets Wrist Wallets</h1>
  <p class="abs hero-sub">ermentum dolor non augue pretium egestas donec est sem eros, tincidunt at congue ut, posuere sit amet</p>
  <ul class="abs hero-list">
    <li><svg width="11" height="8" viewBox="0 0 11 8"><path d="M1 3l3 3 6-5" stroke="#111" stroke-width="2" fill="none"/></svg>Organic Cotton Quorvets</li>
    <li><svg width="11" height="8" viewBox="0 0 11 8"><path d="M1 3l3 3 6-5" stroke="#111" stroke-width="2" fill="none"/></svg>Organic Cotton Quorvets</li>
    <li><svg width="11" height="8" viewBox="0 0 11 8"><path d="M1 3l3 3 6-5" stroke="#111" stroke-width="2" fill="none"/></svg>Touch Mesh Quorvets®</li>
    <li><svg width="11" height="8" viewBox="0 0 11 8"><path d="M1 3l3 3 6-5" stroke="#111" stroke-width="2" fill="none"/></svg>Touch Mesh Quorvets®</li>
  </ul>
  <div class="abs hero-btn">GET IN THOUCH WITH US</div>
</section>

<div class="abs slide-arrow" style="left:108px"><svg width="10" height="12" viewBox="0 0 10 12"><path d="M8 1L2 6l6 5" stroke="#fff" stroke-width="2.4" fill="none"/></svg></div>
<div class="abs slide-arrow" style="left:814px"><svg width="10" height="12" viewBox="0 0 10 12"><path d="M2 1l6 5-6 5" stroke="#fff" stroke-width="2.4" fill="none"/></svg></div>

<section class="abs newsletter">
  <div class="abs label">Our Free Newsletter</div>
  <div class="abs field" style="left:175px;width:166px">Your name</div>
  <div class="abs field" style="left:343px;width:166px">Email Address</div>
  <div class="abs subscribe">SUBSCRIBE NOW</div>
</section>

<h2 class="abs section-title" style="left:147px;top:560px;width:465px">WELCOME TO TANDLO</h2>
<div class="abs more-btn">MORE INFORMATION</div>
<p class="abs intro">Lorem ipsum dolor sit amet, consectetur adipiscing elit. In fermentum dolor non augue pretium egestas. Donec sem eros, tincidunt at congue ut, posuere sit amet est. Vivamus scelerisque viverra odio sit amet laoreet. Ut nec neque non justo rutrum tempor lobortis eu ante. Aliquam sagittis, nibh quis commodo auctor, risus mauris laoreet lectus, id facilisis libero odio nec enim. Sed id ligula adipiscing purus lacinia aliquet it amet laoreet. Ut nec neque non justo rutrum tempor lobortis eu ante. Aliquam sagittis, nibh quis commodo auctor</p>

<h2 class="abs section-title" style="left:147px;top:681px;width:461px">Our Features Products, H2 Heading</h2>

<div class="abs card" style="left:148px;top:714px">
  <div class="pic" role="img" aria-label="Two runners jogging along a lakeshore wearing waist wallets" style="background:linear-gradient(180deg,#d3dbe2 0,#b5c0c7 30%,#8e9ba3 55%,#7a8a63 75%,#5a6a42 100%)"></div>
  <span class="plus">+</span>
</div>
<div class="abs card-title" style="left:148px;top:850px">You Can Take It with You</div>
<div class="abs card-desc" style="left:148px;top:865px">Lorem ipsum dolor sit amet, consectetur adipisicing elit, sed do eiusmod tempor incididunt</div>

<div class="abs card" style="left:385px;top:714px">
  <div class="pic" role="img" aria-label="Smiling man outdoors showing a striped wrist wallet" style="background:linear-gradient(100deg,#5e4e42 0,#9c8471 35%,#bdb5a6 60%,#9a9a92 80%,#7d7f78 100%)"></div>
  <span class="plus">+</span>
</div>
<div class="abs card-title" style="left:385px;top:850px">Quorvets Wrist Wallets</div>
<div class="abs card-desc" style="left:385px;top:865px">Lorem ipsum dolor sit amet, consectetur adipisicing elit, sed do eiusmod tempor incididunt</div>

<h2 class="abs display" style="left:632px;top:559px;font-size:15px;font-weight:400;color:var(--ink)">Look at THAT!</h2>
<div class="abs promo-box">
  <div class="abs promo-art" role="img" aria-label="Product packaging for the Quorvets wrist wallet with an illustrated phone, cards and keys on a dark chalkboard background and a yellow base"></div>
</div>
<div class="abs mini-arrow" style="left:628px"><svg width="6" height="8" viewBox="0 0 6 8"><path d="M5 1L1.5 4 5 7" stroke="#fff" stroke-width="1.6" fill="none"/></svg></div>
<div class="abs mini-arrow" style="left:795px"><svg width="6" height="8" viewBox="0 0 6 8"><path d="M1 1l3.5 3L1 7" stroke="#fff" stroke-width="1.6" fill="none"/></svg></div>

<footer class="abs footer">
  <h3 class="abs foot-head" style="left:149px">Tandlo Information</h3>
  <ul class="abs foot-links" style="left:149px;width:66px">
    <li>Home</li><li>About</li><li>Services</li><li>Press/Media</li><li>Contact</li><li>Blog</li>
  </ul>
  <ul class="abs foot-links" style="left:232px;width:102px">
    <li>Advocates &amp; Affiliates..</li><li>Back Story</li><li>News</li><li>Join Our Mailing List</li><li>Returns/Exchanges</li><li>FAQs</li>
  </ul>

  <h3 class="abs foot-head" style="left:378px">Latest News</h3>
  <div class="abs news" style="top:70px"><div class="date">03 SEP<b>2013</b></div><div class="body"><strong>News Heading Boold</strong><br>Lorem ipsum dolor sit amet, adipisicing elit,<br>sed do eiusmod tempor incididunt ut labore</div></div>
  <div class="abs news" style="top:108px"><div class="date">03 SEP<b>2013</b></div><div class="body"><strong>News Heading Boold</strong><br>Lorem ipsum dolor sit amet, adipisicing elit,<br>sed do eiusmod tempor incididunt ut labore</div></div>
  <div class="abs news" style="top:151px"><div class="date">03 SEP<b>2013</b></div><div class="body"><strong>News Heading Boold</strong><br>Lorem ipsum dolor sit amet, adipisicing elit,<br>sed do eiusmod tempor incididunt ut labore</div></div>

  <h3 class="abs foot-head" style="left:633px">Our Social Share</h3>
  <span class="abs social-ring" style="left:633px" role="img" aria-label="Social network link"></span>
  <span class="abs social-ring" style="left:675px" role="img" aria-label="Social network link"></span>
  <span class="abs social-ring" style="left:717px" role="img" aria-label="Video channel link"></span>
  <span class="abs social-ring" style="left:759px" role="img" aria-label="Social network link"></span>

  <div class="abs contact" style="top:119px">
    <svg width="10" height="10" viewBox="0 0 24 24"><path fill="#fff" d="M6.6 10.8a15 15 0 006.6 6.6l2.2-2.2c.3-.3.7-.4 1-.2 1.1.4 2.3.6 3.6.6.6 0 1 .4 1 1V20c0 .6-.4 1-1 1A17 17 0 013 4c0-.6.4-1 1-1h3.5c.6 0 1 .4 1 1 0 1.3.2 2.5.6 3.6.1.3 0 .7-.2 1z"/></svg>
    <span>555-318-2740 <span class="f">F</span> 555-318-2741</span>
  </div>
  <div class="abs contact" style="top:136px">
    <svg width="11" height="8" viewBox="0 0 11 8"><rect x=".5" y=".5" width="10" height="7" fill="none" stroke="#fff"/><path d="M.5 .5l5 4 5-4" stroke="#fff" fill="none"/></svg>
    <span>sales@tandlo-example.com</span>
  </div>
  <div class="abs connect">GET CONNECT WITH US</div>
</footer>
<div class="abs footer-band"></div>

<p class="abs legal">All right reserved with copyright © 2013 www.tandlo-example.com - Terms</p>
<div class="abs foot-brand">Tandlo</div>

</body>
</html>
```